business card for a massage therapy practice named 'Meadow and Willow Massage Studio'

I really need a trendy, yet easy on the eyes business card to complement my logo. Ideally with some gold or rose gold foil work.

My uploaded file of the logo I have in horizontal but I have a vertical version as well. Another color that is used in the website is a blush pink here and there. I'd like to see some trendy tropical leaves in the design.

```html
<!DOCTYPE html>
<html lang="en">
<head>
<meta charset="utf-8">
<title>Meadow and Willow Massage Studio – Business Card</title>
<link href="https://fonts.googleapis.com/css2?family=Dancing+Script:wght@500&family=Open+Sans:wght@400;600&display=swap" rel="stylesheet">
<style>
  :root {
    --gold: #dbb76c;
    --gold-soft: #e7cd94;
    --ink: #000000;
    --paper: #ffffff;
    --rule: #ddd3c2;
  }
  html, body {
    margin: 0;
    padding: 0;
    width: 972px;
    height: 1200px;
    overflow: hidden;
    background: var(--paper);
  }
  .canvas {
    position: relative;
    width: 972px;
    height: 1200px;
    font-family: "Open Sans", Arial, sans-serif;
  }
  .card {
    position: absolute;
    left: 51px;
    width: 869px;
    height: 508px;
    box-sizing: border-box;
    overflow: hidden;
  }
  .card-front {
    top: 68px;
    background: var(--ink);
  }
  .card-back {
    top: 635px;
    background: var(--paper);
    border: 1px solid var(--rule);
  }
  .foliage {
    position: absolute;
    display: block;
  }
  .foliage-top-right {
    right: 0;
    top: 0;
    width: 207px;
    height: 156px;
  }
  .foliage-bottom-left {
    left: 0;
    bottom: 0;
    width: 136px;
    height: 204px;
  }
  .brand {
    position: absolute;
    left: 0;
    right: 0;
    top: 190px;
    display: flex;
    justify-content: center;
    align-items: center;
    gap: 18px;
    color: var(--gold);
    font-weight: 600;
  }
  .brand-mark {
    width: 46px;
    height: 46px;
    border-radius: 50%;
    background: var(--gold);
    flex: none;
  }
  .brand-name {
    text-align: left;
    line-height: 1.15;
  }
  .brand-title {
    display: block;
    font-size: 40px;
  }
  .brand-subtitle {
    display: block;
    font-size: 20px;
    letter-spacing: 4px;
    text-transform: uppercase;
  }
  .website {
    position: absolute;
    left: 0;
    right: 0;
    top: 354px;
    text-align: center;
    color: var(--paper);
    font-size: 25px;
  }
  .person-name {
    position: absolute;
    left: 0;
    right: 0;
    top: 120px;
    text-align: center;
    font-family: "Dancing Script", cursive;
    font-weight: 500;
    font-size: 72px;
    color: var(--gold);
    line-height: 1;
  }
  .contact {
    position: absolute;
    left: 0;
    right: 0;
    text-align: center;
    color: var(--ink);
  }
  .phone { top: 225px; font-size: 27px; }
  .email { top: 342px; font-size: 25px; }
  .social-mark {
    position: absolute;
    left: 50%;
    top: 385px;
    width: 24px;
    height: 24px;
    margin-left: -12px;
    border-radius: 50%;
    background: var(--gold);
  }
  .handle { top: 418px; font-size: 25px; }
</style>
</head>
<body>
<main class="canvas">
  <section class="card card-front">
    <svg class="foliage foliage-top-right" role="img" aria-label="Gold tropical palm leaves in the top right corner" viewBox="0 0 207 156" preserveAspectRatio="none">
      <defs>
        <linearGradient id="leafFadeTR" x1="1" y1="0" x2="0" y2="1">
          <stop offset="0" stop-color="#dbb76c" stop-opacity="0.9"/>
          <stop offset="1" stop-color="#dbb76c" stop-opacity="0"/>
        </linearGradient>
      </defs>
      <rect width="207" height="156" fill="url(#leafFadeTR)"/>
    </svg>
    <svg class="foliage foliage-bottom-left" role="img" aria-label="Gold tropical palm leaves in the bottom left corner" viewBox="0 0 136 204" preserveAspectRatio="none">
      <defs>
        <linearGradient id="leafFadeBL" x1="0" y1="1" x2="1" y2="0">
          <stop offset="0" stop-color="#dbb76c" stop-opacity="0.9"/>
          <stop offset="1" stop-color="#dbb76c" stop-opacity="0"/>
        </linearGradient>
      </defs>
      <rect width="136" height="204" fill="url(#leafFadeBL)"/>
    </svg>

    <div class="brand">
      <span class="brand-mark" aria-hidden="true"></span>
      <div class="brand-name">
        <span class="brand-title">Meadow &amp; Willow</span>
        <span class="brand-subtitle">Massage Studio</span>
      </div>
    </div>
    <p class="website" style="margin:0">www.meadowandwillow.com</p>
  </section>

  <section class="card card-back">
    <h1 class="person-name" style="margin:0">Lena Marlowe LMT</h1>
    <p class="contact phone" style="margin:0">916 555 0148</p>
    <p class="contact email" style="margin:0">meadowandwillow@mailbox.com</p>
    <span class="social-mark" aria-hidden="true"></span>
    <p class="contact handle" style="margin:0">@meadowandwillow</p>
  </section>
</main>
</body>
</html>
```